Commercial Landscaping Flyer Needed

Looking for a flyer design to showcase what we offer for commercial landscape Installations. We want this to illustrate what sets us apart from our competitors. Include our EMR Safety rating of .72, that our average commercial landscape installation size is $215,000 with our largest completed in 2020 being $1,375,590. We have backgrounds in commercial design and installation and help our customers with Value Engineering Strategies. Since incorporating in 2005, we have an average employment retention length of 8 years. We want this flyer to show our commercial clients that we mean business and are dedicated to making their project happen on time, run efficiently, and we do excellent work.

Need extra days to review

```html
<!DOCTYPE html>
<html lang="en">
<head>
<meta charset="utf-8">
<title>Verdant Row Inc. – Commercial Landscape Installations</title>
<link href="https://fonts.googleapis.com/css2?family=Roboto+Condensed:wght@700&display=swap" rel="stylesheet">
<style>
  :root {
    --page: #ffffff;
    --frame: #c9c9c9;
    --forest: #0d3a30;
    --lime: #c5d930;
    --ink: #111111;
    --text-light: #ffffff;
  }
  * { margin: 0; padding: 0; box-sizing: border-box; }
  html, body { width: 1200px; height: 1000px; overflow: hidden; background: var(--page); }
  body { position: relative; font-family: "Roboto Condensed", "Arial Narrow", sans-serif; font-weight: 700; }

  .flyer {
    position: absolute; left: 230px; top: 22px; width: 740px; height: 956px;
    border: 1px solid var(--frame); overflow: hidden; background: var(--forest);
  }
  .flyer-art { position: absolute; inset: 0; }

  .brand {
    position: absolute; left: 52px; top: 122px; display: flex; align-items: center; gap: 12px;
  }
  .brand-dot { width: 40px; height: 40px; border-radius: 50%; background: var(--lime); }
  .brand-name { font-size: 34px; color: var(--ink); letter-spacing: -0.3px; white-space: nowrap; }

  .headline {
    position: absolute; left: 24px; width: 320px; top: 241px; text-align: center;
    font-size: 22.5px; line-height: 28px; color: var(--ink);
  }

  .fact { position: absolute; color: var(--text-light); font-size: 21.5px; line-height: 26px; white-space: nowrap; }
  .fact-average { left: 432px; top: 616px; }
  .fact-largest { left: 336px; top: 685px; }
  .fact-background { left: 224px; top: 736px; }
  .fact-retention { left: 96px; top: 805px; }
  .fact-dedicated { left: 32px; top: 845px; }

  .contact-bar {
    position: absolute; left: 0; right: 0; bottom: 0; height: 78px; background: var(--forest);
    color: var(--text-light); display: flex; align-items: center; font-size: 20.5px;
  }
  .contact-web { position: absolute; left: 32px; }
  .contact-phones { position: absolute; left: 370px; display: flex; align-items: center; gap: 12px; font-size: 21.5px; }
  .phone-icon { width: 38px; height: 38px; }
</style>
</head>
<body>
  <main class="flyer">
    <svg class="flyer-art" width="740" height="956" viewBox="0 0 740 956">
      <defs>
        <linearGradient id="forestGrad" x1="0" y1="0" x2="0" y2="1">
          <stop offset="0" stop-color="#0d3a30"/>
          <stop offset="1" stop-color="#1c4a38"/>
        </linearGradient>
        <linearGradient id="meadowGrad" x1="0" y1="0" x2="1" y2="1">
          <stop offset="0" stop-color="#2f5a3d"/>
          <stop offset="0.6" stop-color="#4f6b3a"/>
          <stop offset="1" stop-color="#8a7d2e"/>
        </linearGradient>
        <linearGradient id="crewGrad" x1="0" y1="0" x2="0" y2="1">
          <stop offset="0" stop-color="#6f93c0"/>
          <stop offset="0.45" stop-color="#4f6a3f"/>
          <stop offset="1" stop-color="#585a52"/>
        </linearGradient>
        <linearGradient id="courtyardGrad" x1="0" y1="0" x2="1" y2="1">
          <stop offset="0" stop-color="#8d8a7e"/>
          <stop offset="0.5" stop-color="#b2a24a"/>
          <stop offset="1" stop-color="#4c7a3a"/>
        </linearGradient>
        <linearGradient id="gravelGrad" x1="0" y1="0" x2="1" y2="1">
          <stop offset="0" stop-color="#6e7a70"/>
          <stop offset="0.5" stop-color="#9c8f80"/>
          <stop offset="1" stop-color="#7a6c5e"/>
        </linearGradient>
        <linearGradient id="shieldGrad" x1="0" y1="0" x2="1" y2="0">
          <stop offset="0.5" stop-color="#2f6fc0"/>
          <stop offset="0.5" stop-color="#1d4f9e"/>
        </linearGradient>
      </defs>

      <rect width="740" height="956" fill="url(#forestGrad)"/>
      <rect class="meadow-photo" x="0" y="700" width="740" height="180" fill="url(#meadowGrad)" opacity="0.8"
            role="img" aria-label="Photo of a planted meadow with yellow wildflowers"/>
      <path d="M0,0 L552,0 Q430,95 372,214 L216,376 Q120,414 0,424 Z" fill="#ffffff"/>

      <path d="M552,0 L740,0 L740,256 Q700,305 640,362 L380,204 Q440,90 552,0 Z"
            fill="url(#crewGrad)" stroke="#ffffff" stroke-width="8"
            role="img" aria-label="Photo of a crew in safety vests planting a street tree"/>
      <path d="M0,424 Q120,414 216,378 L360,666 Q190,720 0,738 Z"
            fill="url(#gravelGrad)" stroke="#d6d6d6" stroke-width="8"
            role="img" aria-label="Photo of ornamental grasses in a gravel bed beside a fuel price sign"/>
      <path d="M372,218 L640,368 L368,638 L216,376 Z"
            fill="url(#courtyardGrad)" stroke="#d6d6d6" stroke-width="8"
            role="img" aria-label="Aerial photo of a landscaped apartment courtyard in a city"/>

      <g class="safety-shield" transform="translate(525,372)">
        <path d="M90,0 L180,26 Q182,150 90,228 Q-2,150 0,26 Z" fill="#c4ccd6"/>
        <path d="M90,12 L168,34 Q168,142 90,212 Q12,142 12,34 Z" fill="url(#shieldGrad)"/>
        <text x="90" y="114" text-anchor="middle" fill="#ffffff" font-family="Roboto Condensed, sans-serif" font-weight="700" font-size="86">.72</text>
        <path d="M-6,138 L186,124 L186,156 L-6,170 Z" fill="#1d3f86" stroke="#ffffff" stroke-width="2"/>
        <text x="90" y="155" text-anchor="middle" fill="#ffffff" font-family="Roboto Condensed, sans-serif" font-weight="700" font-size="15" letter-spacing="1" transform="rotate(-4 90 150)">EMR SAFETY RATING</text>
      </g>
    </svg>

    <div class="brand">
      <span class="brand-dot"></span>
      <span class="brand-name">Verdant Row Inc.</span>
    </div>

    <h1 class="headline">COMMERCIAL LANDSCAPE<br>INSTALLATIONS</h1>

    <p class="fact fact-average">Average commercial landscape<br>Installation size $215,000</p>
    <p class="fact fact-largest">Our largest completed in 2020&nbsp; $1,375,590</p>
    <p class="fact fact-background">Backgrounds in commercial design and installation and<br>value engineering strategies for our customers</p>
    <p class="fact fact-retention">Incorporated 2005. Average employment retention length of 8 years</p>
    <p class="fact fact-dedicated">Dedicated to making projects on time. Efficiently run.</p>

    <footer class="contact-bar">
      <span class="contact-web">www.verdantrowinc.com</span>
      <span class="contact-phones">
        <svg class="phone-icon" viewBox="0 0 38 38">
          <circle cx="19" cy="19" r="17" fill="none" stroke="#ffffff" stroke-width="2.5"/>
          <path d="M13,10 L16,10 L17.5,15 L15.5,16.5 Q17.5,21 21.5,22.5 L23,20.5 L28,22 L28,25 Q27,28 24,28 Q11,26 10,13 Q10,10 13,10 Z" fill="#ffffff"/>
        </svg>
        (555) 764-0131 (555) 492-0126
      </span>
    </footer>
  </main>
</body>
</html>
```